Halvery Metal Recyclers - www.halveryrecyclers.com.au

I've just rebranded my business and thought what better way to continue with this than getting a website.
It is going to be fairly basic for now. I've attached quite a few images, feel free to use whichever you like.
And pages description is also attached in a .doc file.
Updates

Hi, this is my first time having a website. I am open to anything and trust the experience and ideas you can bring forward. I will look at extending the deadline so I can take my time to give feedback as needed! Thank you all.

Target Market(s)

Mining and industrial and commercial sectors

Coding

Coded - Design and coding required

Number of Pages Required

5+ page

Requirements
Must have
• Logo/Phone number at the top of every page. "Scrap Metal Specialists" tag line at the top of every page.
Nice to have
• Top Navigation.

```html
<!DOCTYPE html>
<html lang="en">
<head>
<meta charset="utf-8">
<title>Halvery Metal Recyclers</title>
<link href="https://fonts.googleapis.com/css2?family=Jost:wght@400;500&family=Roboto:wght@500;700&family=Staatliches&display=swap" rel="stylesheet">
<style>
:root{
  --navy:#17386a;
  --navy-dark:#122d56;
  --ink:#1f2328;
  --text:#4a4f57;
  --white:#ffffff;
  --mist:#e6ebf3;
  --footer:#121521;
  --footer-line:#3a3f4d;
  --steel:#d9d9d9;
  --rust:#a8582c;
}
*{margin:0;padding:0;box-sizing:border-box}
html,body{width:1200px;height:3451px;overflow:hidden}
body{position:relative;font-family:"Jost",sans-serif;color:var(--ink);background:var(--white)}
.abs{position:absolute}
.display{font-family:"Staatliches",sans-serif;font-weight:400;letter-spacing:.5px}

/* top bar */
.topbar{left:0;top:0;width:1200px;height:39px;background:var(--navy);color:var(--white);font-family:"Roboto",sans-serif;font-weight:500;font-size:14px}
.topbar .tagline{left:0;width:1200px;text-align:center;top:11px}
.topbar .phone{left:968px;top:10px;font-weight:700;font-size:16px;display:flex;align-items:center;gap:6px}

/* header */
.header{left:0;top:39px;width:1200px;height:98px;background:var(--white)}
.brand{left:99px;top:26px;color:var(--navy);font-weight:500;font-size:22px;line-height:24px}
.nav{right:99px;top:38px;display:flex;gap:44px;font-size:16px;color:#6b7078}
.nav a{color:inherit;text-decoration:none}
.nav .active{color:var(--navy);font-weight:500}

/* hero */
.hero{left:0;top:137px;width:1200px;height:582px;background:radial-gradient(ellipse at 60% 55%,#7a3418 0%,#3a1d14 45%,#17120f 100%)}
.hero .arrow{top:290px}

/* welcome */
.welcome-kicker{left:99px;top:908px;font-size:32px;color:var(--ink)}
.welcome-title{left:99px;top:948px;font-size:56px;color:var(--ink);line-height:60px}
.welcome-text{left:99px;top:1020px;width:540px;font-size:17.5px;line-height:26px;color:var(--text)}
.portrait{left:687px;top:810px;width:337px;height:498px;background:linear-gradient(180deg,#e4e4e4 0%,#cfcfcf 55%,#9ea0a3 100%)}

.btn{display:flex;align-items:center;justify-content:space-between;font-family:"Roboto",sans-serif;font-weight:700;font-size:15px;padding:0 4px 0 25px;height:44px;width:162px}
.btn .ico{width:32px;height:32px;display:flex;align-items:center;justify-content:center}
.btn-solid{background:var(--navy);color:var(--white);border:2px solid var(--navy)}
.btn-solid .ico{background:var(--white);color:var(--navy)}
.btn-line{border:2px solid var(--white);color:var(--white)}
.btn-line .ico{background:var(--white);color:var(--navy)}

/* services */
.services{left:0;top:1402px;width:1200px;height:656px;background:var(--navy)}
.section-title{width:1200px;left:0;text-align:center;font-size:64px}
.services .section-title{top:50px;color:var(--white)}
.svc{width:316px;color:var(--white)}
.svc .photo{width:316px;height:221px;border-radius:24px 0 24px 0}
.svc h3{font-weight:500;font-size:24px;line-height:34px;margin-top:12px}
.svc p{font-size:17.5px;line-height:27px;color:#dfe5ef;margin-top:8px}

/* blog */
.blog .section-title{top:2170px;color:var(--ink)}
.post{width:238px;height:250px;top:2263px}
.post .photo{width:238px;height:187px}
.post .caption{position:absolute;left:0;top:151px;width:180px;background:var(--white);padding:8px 12px 0 12px;font-weight:500;font-size:17px;line-height:23px;color:var(--ink)}
.post .more{position:absolute;left:14px;top:218px;font-family:"Roboto",sans-serif;font-weight:500;font-size:14px;color:var(--navy);border-bottom:1.5px solid var(--navy);padding-bottom:2px;display:flex;gap:6px;align-items:center}
.slide-btn{width:38px;height:38px;border-radius:50%;display:flex;align-items:center;justify-content:center;top:2347px}

/* contact */
.contact{left:0;top:2619px;width:1200px;height:441px;background:var(--mist)}
.contact .strip{left:0;top:0;width:186px;height:441px;background:var(--navy)}
.contact .photo{left:99px;top:55px;width:356px;height:319px;border-radius:0 0 40px 0;background:linear-gradient(180deg,#6b9ccc 0%,#7d6a4e 35%,#8a4a2a 62%,#c47a3a 100%)}
.contact h2{left:492px;top:98px;font-size:46px;color:var(--ink)}
.field{background:var(--white);border:1px solid #cfd6e0;font-size:14px;color:#6b7078;padding:10px 11px;width:304px;height:41px}
.submit{left:482px;top:2919px;width:145px;height:44px;background:var(--navy);color:var(--white);font-family:"Roboto",sans-serif;font-weight:700;font-size:16px;display:flex;align-items:center;justify-content:space-between;padding:0 4px 0 29px}
.submit .ico{width:32px;height:32px;background:var(--white);color:var(--navy);display:flex;align-items:center;justify-content:center}

/* footer */
.footer{left:0;top:3060px;width:1200px;height:391px;background:var(--footer);color:var(--white)}
.footer .brand-foot{left:99px;top:100px;font-weight:500;font-size:30px;line-height:34px}
.footer h4{font-family:"Staatliches",sans-serif;font-weight:400;font-size:21px}
.links{left:421px;top:60px}
.links ul{list-style:none;margin-top:12px}
.links li{font-size:17px;line-height:34px;color:#c9cdd6}
.vline{width:1px;background:var(--footer-line);top:60px;height:230px}
.vline::after{content:"";position:absolute;left:-2px;top:55px;width:5px;height:24px;background:var(--white)}
.info{left:646px;top:60px}
.info .name{font-weight:500;font-size:17px;margin-top:14px}
.info .row{display:flex;align-items:center;gap:12px;font-size:17px;color:#c9cdd6;margin-top:14px;padding-left:7px}
.social{left:984px;top:144px;display:flex;gap:11px}
.social span{width:32px;height:32px;border-radius:50%;background:var(--white);display:block}
.footer .rule{left:99px;top:325px;width:1002px;height:1px;background:var(--footer-line)}
.copy{left:0;width:1200px;top:349px;text-align:center;font-size:15px;color:#b9bec8}
.copy b{font-weight:500;color:var(--white)}
</style>
</head>
<body>

<div class="topbar abs">
  <div class="tagline abs">Scrap Metal Specialists</div>
  <div class="phone abs">
    <svg width="14" height="14" viewBox="0 0 24 24"><path fill="#fff" d="M6.6 10.8a15.2 15.2 0 0 0 6.6 6.6l2.2-2.2c.3-.3.7-.4 1-.2 1.1.4 2.3.6 3.6.6.6 0 1 .4 1 1V20c0 .6-.4 1-1 1A17 17 0 0 1 3 4c0-.6.4-1 1-1h3.5c.6 0 1 .4 1 1 0 1.3.2 2.5.6 3.6.1.3 0 .7-.2 1z"/></svg>
    0491570362
  </div>
</div>

<header class="header abs">
  <div class="brand abs">Halvery<br>Metal Recyclers</div>
  <nav class="nav abs">
    <a class="active">Home</a><a>About</a><a>Services</a><a>Online Store</a><a>Blog</a><a>Contact</a>
  </nav>
</header>

<section class="hero abs" role="img" aria-label="Worker oxy cutting steel with sparks, overlaid with large company name lettering">
  <svg class="arrow abs" style="left:98px" width="32" height="58" viewBox="0 0 32 58"><polyline points="30,2 3,29 30,56" fill="none" stroke="#fff" stroke-width="2"/></svg>
  <svg class="arrow abs" style="left:1071px" width="32" height="58" viewBox="0 0 32 58"><polyline points="2,2 29,29 2,56" fill="none" stroke="#fff" stroke-width="2"/></svg>
</section>

<section class="welcome">
  <div class="welcome-kicker abs display">Welcome to</div>
  <h1 class="welcome-title abs display">Halvery Metal Recyclers</h1>
  <p class="welcome-text abs">Welcome to the website of Halvery Metal Recyclers. We are a Perth based company that provides scrap metal collection and oxy cutting services in the mining, construction</p>
  <div class="btn btn-solid abs" style="left:99px;top:1121px">Read More<span class="ico"><svg width="16" height="14" viewBox="0 0 16 14"><path d="M1 7h13M8 1l6 6-6 6" fill="none" stroke="currentColor" stroke-width="2"/></svg></span></div>
  <div class="portrait abs" role="img" aria-label="Portrait of the business owner in a grey blazer, arms crossed"></div>
</section>

<section class="services abs">
  <h2 class="section-title abs display">Our Services</h2>
  <article class="svc abs" style="left:99px;top:139px">
    <div class="photo" role="img" aria-label="Worker oxy cutting metal with bright sparks" style="background:linear-gradient(160deg,#2a1a12 0%,#5a2a14 55%,#d8641c 100%)"></div>
    <h3>Oxy cutting and breaking down</h3>
    <p>Lorem ipsum dolor sit amet, concteture adipiscing elit. In ultrices velit ut ante commodo</p>
  </article>
  <div class="btn btn-line abs" style="left:99px;top:538px">Read More<span class="ico"><svg width="16" height="14" viewBox="0 0 16 14"><path d="M1 7h13M8 1l6 6-6 6" fill="none" stroke="currentColor" stroke-width="2"/></svg></span></div>

  <article class="svc abs" style="left:442px;top:139px">
    <div class="photo" role="img" aria-label="Large mining excavator machinery in an open pit" style="background:linear-gradient(180deg,#8fa07a 0%,#9c8a6a 40%,#b39a74 100%)"></div>
    <h3>Large mining machinery</h3>
    <p>Lorem ipsum dolor sit amet, consectetur adipiscing elit. In ultrices velit ut ante commodo, quis consequat elit auctor. Vivamus rhoncus, quam</p>
  </article>
  <div class="btn btn-line abs" style="left:442px;top:538px">Read More<span class="ico"><svg width="16" height="14" viewBox="0 0 16 14"><path d="M1 7h13M8 1l6 6-6 6" fill="none" stroke="currentColor" stroke-width="2"/></svg></span></div>

  <article class="svc abs" style="left:785px;top:139px">
    <div class="photo" role="img" aria-label="Yellow minesite hydraulic equipment dismantled on gravel" style="background:linear-gradient(150deg,#8f8a80 0%,#c9a94a 50%,#6d6760 100%)"></div>
    <h3>Large minesite infrastructure</h3>
    <p>Lorem ipsm dolor sit amet, consectetur adipiscing elit. In ultrices velit ut ante commodo, quis consequat elit auctor. Vivamus rhoncus, quam</p>
  </article>
  <div class="btn btn-line abs" style="left:785px;top:538px">Read More<span class="ico"><svg width="16" height="14" viewBox="0 0 16 14"><path d="M1 7h13M8 1l6 6-6 6" fill="none" stroke="currentColor" stroke-width="2"/></svg></span></div>
</section>

<section class="blog">
  <h2 class="section-title abs display">Latest Blog</h2>
  <article class="post abs" style="left:99px">
    <div class="photo" role="img" aria-label="Row of corrugated steel sections in a yard" style="background:linear-gradient(180deg,#b9bcbf 0%,#7e7f80 100%)"></div>
    <div class="caption">Duis tincidunt arcu a orci accumsan</div>
    <div class="more">Read More <svg width="11" height="9" viewBox="0 0 16 14"><path d="M1 7h13M8 1l6 6-6 6" fill="none" stroke="currentColor" stroke-width="2"/></svg></div>
  </article>
  <article class="post abs" style="left:353px">
    <div class="photo" role="img" aria-label="Cut steel shaft lying in dirt" style="background:linear-gradient(160deg,#9a6a4e 0%,#b0b3b3 55%,#6f6a63 100%)"></div>
    <div class="caption">Duis tincidunt arcu a orci accumsan</div>
    <div class="more">Read More <svg width="11" height="9" viewBox="0 0 16 14"><path d="M1 7h13M8 1l6 6-6 6" fill="none" stroke="currentColor" stroke-width="2"/></svg></div>
  </article>
  <article class="post abs" style="left:607px">
    <div class="photo" role="img" aria-label="Rusted steel bin on orange ground under trees" style="background:linear-gradient(180deg,#6e9bc9 0%,#7a5440 45%,#c98a46 100%)"></div>
    <div class="caption">Duis tincidunt arcu a orci accumsan</div>
    <div class="more">Read More <svg width="11" height="9" viewBox="0 0 16 14"><path d="M1 7h13M8 1l6 6-6 6" fill="none" stroke="currentColor" stroke-width="2"/></svg></div>
  </article>
  <article class="post abs" style="left:861px">
    <div class="photo" role="img" aria-label="Large rusted slewing ring gear on gravel" style="background:linear-gradient(180deg,#9c8672 0%,#5e4a3c 50%,#8c7460 100%)"></div>
    <div class="caption">Duis tincidunt arcu a orci accumsan</div>
    <div class="more">Read More <svg width="11" height="9" viewBox="0 0 16 14"><path d="M1 7h13M8 1l6 6-6 6" fill="none" stroke="currentColor" stroke-width="2"/></svg></div>
  </article>
  <div class="slide-btn abs" style="left:81px;background:var(--white)"><svg width="10" height="16" viewBox="0 0 10 16"><polyline points="8,2 2,8 8,14" fill="none" stroke="#17386a" stroke-width="2.5"/></svg></div>
  <div class="slide-btn abs" style="left:1081px;background:var(--navy)"><svg width="10" height="16" viewBox="0 0 10 16"><polyline points="2,2 8,8 2,14" fill="none" stroke="#fff" stroke-width="2.5"/></svg></div>
</section>

<section class="contact abs">
  <div class="strip abs"></div>
  <div class="photo abs" role="img" aria-label="Rusted steel skip bin on red earth under blue sky"></div>
  <h2 class="abs display">Get in Touch</h2>
  <div class="field abs" style="left:482px;top:147px">Name</div>
  <div class="field abs" style="left:482px;top:194px">Email</div>
  <div class="field abs" style="left:482px;top:241px">Phone</div>
  <div class="field abs" style="left:797px;top:147px;height:135px">Your Message</div>
</section>
<div class="submit abs">Submit<span class="ico"><svg width="16" height="14" viewBox="0 0 16 14"><path d="M1 7h13M8 1l6 6-6 6" fill="none" stroke="currentColor" stroke-width="2"/></svg></span></div>

<footer class="footer abs">
  <div class="brand-foot abs">Halvery<br>Metal Recyclers</div>
  <div class="links abs">
    <h4>Quick Links</h4>
    <ul><li>Home</li><li>About</li><li>Services</li><li>Online Store</li><li>Blog</li><li>Contact</li></ul>
  </div>
  <div class="vline abs" style="left:584px"></div>
  <div class="info abs">
    <h4>Contact Info</h4>
    <div class="name">Cal Ashby</div>
    <div class="row"><svg width="16" height="16" viewBox="0 0 24 24"><path fill="#fff" d="M6.6 10.8a15.2 15.2 0 0 0 6.6 6.6l2.2-2.2c.3-.3.7-.4 1-.2 1.1.4 2.3.6 3.6.6.6 0 1 .4 1 1V20c0 .6-.4 1-1 1A17 17 0 0 1 3 4c0-.6.4-1 1-1h3.5c.6 0 1 .4 1 1 0 1.3.2 2.5.6 3.6.1.3 0 .7-.2 1z"/></svg>0491570362</div>
    <div class="row"><svg width="16" height="12" viewBox="0 0 16 12"><rect width="16" height="12" rx="1" fill="#fff"/><polyline points="1,1 8,7 15,1" fill="none" stroke="#121521" stroke-width="1.5"/></svg>cal@halveryrecyclers.com.au</div>
  </div>
  <div class="vline abs" style="left:944px"></div>
  <div class="social abs" aria-label="Social links"><span></span><span></span><span></span></div>
  <div class="rule abs"></div>
  <div class="copy abs">© 2022 <b>Halvery Metal Recyclers</b> . All right reserved</div>
</footer>

</body>
</html>
```